Women Web Portal

We are developing an internet portal with content created by and for women in Latin America.
This portal will contain different categories focused on relevant topics for women who are at the same time mothers, lovers, workers, pet-owners, ...

We are looking for design that are at the same time uncluttered, easy-to-use and obvious, and comfy. Pastel colours, buttons using traditional fonts, large space for pictures, highlighted social elements,...

Our target being the middle-class women, we want a design that feels comfortable, real, a bit trendy and traditional, not a Tarsk & Welmore design, something women can relate to and feel comfortable enough to come back and participate.

Examples of websites:
www.dishtable.example
mujer.qelvo.example
www.cabellorinva.example
www.fourneau.example
Updates

Hi dear designers. After viewing some first drafts, I have updated the brief so you might have a better understanding of what we are looking for.

Thanks

Reason: We've been away for a while, unavailable to provide adequate feedback to the designs already sent. So we're extending the deadline in order to give time to everyone to adapt their work according to the feedback we'll be providing today.

Target Market(s)

Women between 25 and 50 years from Latin America. Mainly mothers: basically, we want women to interact with each other and with the content of the site so they create a strong community.

Advertisingly speaking, we want to have users, contents and FMCG brands to live together on this website.

Industry/Entity Type

Internet

Requirements
Must have
• Pastel colours for category tabs. Comfortable look & feel.

The design should include 3 different pages:
- Homepage
- Article page
- User profile

The page will be done in responsive design, so design should be thought to be adapted according to the browser (2 or 3 columns).

Thanks for doing it as a PSD file .

The design should also include:
- 8 category tabs
- Space for 728x90px and 300x600px advertising format.
- A relevant menu bar at the beginning of each page
Nice to have
• News feed/best content/most active comments zone: we need to bring forward content to our users so they'll be attracted to visit more pages of the website.

Small format to register (account).

Slider or any other moving objects.

Any idea that would facilitate and increase user participation
Should not have
• Actual text. please use Lorem Ipsum.

```html
<!DOCTYPE html>
<html lang="en">
<head>
<meta charset="utf-8">
<title>Women Web Portal – Home</title>
<link href="https://fonts.googleapis.com/css2?family=Arimo:wght@400;700&display=swap" rel="stylesheet">
<style>
:root{
  --pink:#e0287f;
  --pink-soft:#ec5aa0;
  --ink:#222;
  --muted:#8a8a8a;
  --line:#e4e4e4;
  --panel:#f3f3f3;
  --black:#0b0b0b;
  --white:#fff;
  --blue:#3b5b9a;
  --red:#d2322d;
  --orange:#ef7d22;
  --sky:#5fc6e6;
}
*{box-sizing:border-box;margin:0;padding:0}
html,body{width:1200px;height:2931px;overflow:hidden}
body{position:relative;background:var(--white);font-family:"Arimo",Arial,sans-serif;color:var(--ink)}
.abs{position:absolute}
.photo{position:absolute}
/* top bar */
.topbar{left:0;top:0;width:1200px;height:43px;background:var(--pink)}
.topbar .net{left:32px;top:14px;color:var(--white);font-size:13px;font-weight:700}
.topbar .ico{top:8px;width:26px;height:26px;border-radius:4px;background:rgba(255,255,255,.85)}
.topbar .acct{top:14px;color:var(--white);font-size:13px}
.topbar .search{left:922px;top:7px;width:243px;height:28px;background:var(--white);border-radius:3px;font-size:12px;color:var(--muted);padding:7px 10px}
.topbar .search svg{position:absolute;right:8px;top:5px}
/* header */
.logo{left:30px;top:102px;color:var(--pink);font-size:35px;font-weight:700;letter-spacing:.5px}
.slogan{left:66px;top:144px;color:var(--muted);font-size:13px}
.nav{top:104px;height:33px;font-size:14px;color:var(--muted);line-height:33px}
.nav.active{left:394px;width:71px;background:var(--pink);color:var(--white);text-align:center;border-radius:3px}
.ad-leader{left:178px;top:213px;width:844px;height:92px;background:var(--black);border-radius:6px;color:#bbb;font-size:25px;text-align:center;line-height:92px}
/* slider */
.slider{left:30px;top:371px;width:1137px;height:381px;border:1px solid var(--line)}
.slide-main{left:43px;top:384px;width:753px;height:356px;background:linear-gradient(120deg,#6d4b3a 0%,#b9876b 40%,#d9a44a 70%,#e2c48a 100%)}
.arrow{width:52px;height:52px;border-radius:50%;background:rgba(0,0,0,.25)}
.thumb{left:808px;width:117px;height:92px;border:2px solid var(--line)}
.thumb-title{left:950px;font-size:13px;color:#444}
.thumb-text{left:950px;width:210px;font-size:12px;line-height:19px;color:#444}
/* tabs */
.tabs{left:30px;top:790px;width:743px;height:41px;background:linear-gradient(#ef6cad,var(--pink));border-radius:4px;display:flex;font-size:13px;color:var(--white);line-height:41px}
.tabs span{padding:0 13px}
.tabs .on{background:var(--black);border-radius:4px 0 0 4px;width:102px;text-align:center}
.section-title{font-size:23px;color:var(--pink)}
.intro-title{left:808px;top:788px;font-size:23px;color:#222}
.video{background:var(--black);border-radius:2px}
.ad-sky{left:808px;top:1083px;width:359px;height:620px;background:var(--black);color:#ccc;font-size:33px;text-align:center;padding-top:244px;line-height:44px}
/* grid */
.grid{left:30px;top:859px;width:743px;height:699px;border:1px solid var(--line);border-radius:4px}
.grid-text{width:346px;font-size:12.5px;line-height:21px;color:#333}
.bar{height:15px;background:var(--panel)}
/* news */
.news-thumb{left:43px;width:82px;height:76px}
.news-head{left:145px;font-size:17px;color:#333}
.news-date{left:145px;font-size:11.5px;color:var(--muted)}
.news-text{left:145px;width:610px;font-size:12px;line-height:21px;color:#333}
.more{left:688px;font-size:12px;color:var(--pink);text-decoration:underline}
.rule{left:43px;width:716px;height:1px;background:var(--line)}
/* share */
.share{left:808px;top:1734px;width:359px;height:346px;background:var(--panel);border:1px solid var(--line)}
.sbtn{width:142px;height:41px;border-radius:4px;color:var(--white);font-size:17px;font-weight:700;line-height:41px;padding-left:58px}
.sbtn i{position:absolute;left:8px;top:7px;width:27px;height:27px;background:rgba(255,255,255,.9);border-radius:3px}
.sbtn.light{background:var(--white);border:1px solid #ccc;color:#333}
.sbtn.light i{background:#bbb}
.likeus{left:858px;top:1968px;font-size:17px;font-weight:700;color:var(--blue)}
.likeus i{position:absolute;left:54px;top:-6px;width:36px;height:36px;border:1px solid #bbb;border-radius:3px;background:var(--white)}
.follow{left:918px;top:2016px;width:149px;height:43px;background:var(--sky);border-radius:4px;color:var(--white);font-size:12px;text-align:center;line-height:15px;padding-top:7px}
/* comment form */
.field{left:43px;width:338px;height:31px;background:var(--panel);font-size:13px;padding:8px 12px;color:#333}
.area{left:422px;top:2222px;width:341px;height:117px;background:var(--panel);font-size:13px;padding:10px 20px;color:#333}
.post{left:341px;top:2366px;width:122px;height:34px;background:var(--panel);font-size:12px;color:#999;text-align:center;line-height:34px}
.t-thumb{left:813px;width:64px;height:62px}
.t-name{left:885px;font-size:13px;color:#444}
.t-date{left:885px;font-size:11px;color:var(--muted)}
.t-text{left:885px;width:275px;font-size:12px;line-height:18px;color:#333}
.t-like{left:955px;font-size:11px;color:var(--muted)}
.t-like i{display:inline-block;width:14px;height:14px;background:var(--blue);border-radius:2px;vertical-align:middle;margin-left:8px}
.t-com{left:1090px;font-size:12px;color:var(--muted);text-decoration:underline}
.vcap{font-size:12.5px;color:#222}
.vcap em{font-style:normal;color:var(--pink);margin-left:14px}
.footer{left:0;top:2799px;width:1200px;height:132px;background:var(--black)}
.flinks{left:0;top:2838px;width:1200px;text-align:center;font-size:12px;color:var(--white);word-spacing:2px}
.flinks span{margin:0 13px}
.copy{left:0;top:2888px;width:1200px;text-align:center;font-size:12px;color:var(--white)}
.play{position:absolute;left:50%;top:50%;width:36px;height:36px;margin:-18px 0 0 -18px;border-radius:50%;background:var(--red)}
.play::after{content:"";position:absolute;left:14px;top:10px;border-left:12px solid var(--white);border-top:8px solid transparent;border-bottom:8px solid transparent}
</style>
</head>
<body>

<header>
  <div class="abs topbar">
    <div class="abs net">NETWORK WITH US</div>
    <span class="abs ico" style="left:172px"></span>
    <span class="abs ico" style="left:205px"></span>
    <span class="abs ico" style="left:238px"></span>
    <span class="abs ico" style="left:271px"></span>
    <div class="abs acct" style="left:755px">Register</div>
    <div class="abs acct" style="left:823px;border-left:1px solid rgba(255,255,255,.6);padding-left:26px;left:826px">Sign in</div>
    <div class="abs search">Search any keyword here
      <svg width="20" height="20" viewBox="0 0 20 20"><circle cx="8" cy="8" r="6" fill="none" stroke="#888" stroke-width="2"/><line x1="12.5" y1="12.5" x2="18" y2="18" stroke="#888" stroke-width="2.5"/></svg>
    </div>
  </div>

  <div class="abs logo">LOGO GOES HERE</div>
  <div class="abs slogan">SLOGAN GOES HERE</div>

  <nav>
    <div class="abs nav active">HOME</div>
    <div class="abs nav" style="left:486px">ABOUT US</div>
    <div class="abs nav" style="left:584px">SERVICES</div>
    <div class="abs nav" style="left:683px">WOMEN HEATH</div>
    <div class="abs nav" style="left:816px">PET CARE</div>
    <div class="abs nav" style="left:917px">CONTACT US</div>
  </nav>

  <div class="abs ad-leader">728 X 90&nbsp; ADVERTISEMANT AREA</div>
</header>

<main>
  <section>
    <div class="abs slider"></div>
    <div class="slide-main" style="position:absolute" role="img" aria-label="Featured photo of a young couple with a red rose"></div>
    <div class="abs arrow" style="left:55px;top:536px"><svg width="52" height="52"><polyline points="30,17 21,26 30,35" fill="none" stroke="#fff" stroke-width="3"/></svg></div>
    <div class="abs arrow" style="left:731px;top:536px"><svg width="52" height="52"><polyline points="22,17 31,26 22,35" fill="none" stroke="#fff" stroke-width="3"/></svg></div>

    <div class="photo thumb" style="top:386px;background:linear-gradient(120deg,#7a5443,#d2a269)" role="img" aria-label="Couple with rose thumbnail"></div>
    <div class="abs thumb-title" style="top:392px">HEADIGN GOES HERE</div>
    <div class="abs thumb-text" style="top:422px">"But I must explain to you how all this mistaken idea of denouncing</div>

    <div class="photo thumb" style="top:514px;background:linear-gradient(120deg,#e9c6b6,#f6e6dc)" role="img" aria-label="Mother and baby thumbnail"></div>
    <div class="abs thumb-title" style="top:514px">HEADIGN GOES HERE</div>
    <div class="abs thumb-text" style="top:552px">"But I must explain to you how all this mistaken idea of denouncing</div>

    <div class="photo thumb" style="top:648px;background:linear-gradient(120deg,#f1ddd2,#b86a45)" role="img" aria-label="Smiling woman thumbnail"></div>
    <div class="abs thumb-title" style="top:654px">HEADIGN GOES HERE</div>
    <div class="abs thumb-text" style="top:693px">"But I must explain to you how all this mistaken idea of denouncing</div>
  </section>

  <section>
    <div class="abs tabs">
      <span class="on">Love</span><span>Category2</span><span>Category3</span><span>Category4</span><span>Category5</span><span>Category6</span><span>Category7</span><span>Category8</span>
    </div>
    <div class="abs grid"></div>

    <div class="photo" style="left:43px;top:869px;width:346px;height:214px;background:linear-gradient(160deg,#eef1f4,#c9a993)" role="img" aria-label="Couple lying together photo"></div>
    <div class="photo" style="left:414px;top:869px;width:346px;height:214px;background:linear-gradient(160deg,#4a5a3a,#6d7a57 60%,#3e4a36)" role="img" aria-label="Woman reading by a stream photo"></div>
    <div class="abs grid-text" style="left:43px;top:1098px">"But I must explain to you how all this mistaken idea of denouncing pleasure and praising pain was born and I will</div>
    <div class="abs grid-text" style="left:414px;top:1098px">"But I must explain to you how all this mistaken idea of denouncing pleasure and praising pain was born and I will</div>
    <div class="abs bar" style="left:43px;top:1172px;width:717px"></div>

    <div class="photo" style="left:43px;top:1223px;width:346px;height:216px;background:radial-gradient(circle at 55% 45%,#c79a5a,#3b2a18 55%,#120d08)" role="img" aria-label="Couple under an umbrella at night photo"></div>
    <div class="photo" style="left:414px;top:1223px;width:346px;height:216px;background:linear-gradient(120deg,#6d4b3a,#b9876b 50%,#d9a44a)" role="img" aria-label="Couple with red rose photo"></div>
    <div class="abs grid-text" style="left:43px;top:1455px">"But I must explain to you how all this mistaken idea of denouncing pleasure and praising pain was born and I will</div>
    <div class="abs grid-text" style="left:414px;top:1455px">"But I must explain to you how all this mistaken idea of denouncing pleasure and praising pain was born and I will</div>
    <svg class="abs" style="left:378px;top:1540px" width="38" height="38" viewBox="0 0 38 38"><circle cx="19" cy="19" r="17" fill="#fff" stroke="#ccc" stroke-width="1.5"/><polyline points="12,16 19,23 26,16" fill="none" stroke="#aaa" stroke-width="2"/></svg>
  </section>

  <aside>
    <div class="abs intro-title">INTRODUCTION</div>
    <div class="abs video" style="left:808px;top:841px;width:359px;height:211px"><span class="play"></span></div>
    <div class="abs ad-sky">300 x 600<br>Advertisement Area</div>
  </aside>

  <section>
    <div class="abs section-title" style="left:30px;top:1632px">LATEST NEWS</div>

    <div class="photo news-thumb" style="top:1687px;background:linear-gradient(135deg,#d6b08e,#8a5a3e)" role="img" aria-label="News author portrait"></div>
    <div class="abs news-head" style="top:1686px">Head line Goes Here</div>
    <div class="abs news-date" style="top:1712px">My 5-2013 , Sunday 9:11 pm</div>
    <div class="abs news-text" style="top:1730px">"But I must explain to you how all this mistaken idea of denouncing pleasure and praising pain was born and I will give you a complete account of the system, and expound the actual teachings of the g</div>
    <div class="abs more" style="top:1751px">READ MORE</div>
    <div class="abs rule" style="top:1798px"></div>

    <div class="photo news-thumb" style="top:1820px;background:linear-gradient(135deg,#d6b08e,#8a5a3e)" role="img" aria-label="News author portrait"></div>
    <div class="abs news-head" style="top:1820px">Head line Goes Here</div>
    <div class="abs news-date" style="top:1846px">My 5-2013 , Sunday 9:11 pm</div>
    <div class="abs news-text" style="top:1864px">"But I must explain to you how all this mistaken idea of denouncing pleasure and praising pain was born and I will give you a complete account of the system, and expound the actual teachings of the g</div>
    <div class="abs more" style="top:1885px">READ MORE</div>
    <div class="abs rule" style="top:1927px"></div>

    <div class="photo news-thumb" style="top:1945px;background:linear-gradient(135deg,#d6b08e,#8a5a3e)" role="img" aria-label="News author portrait"></div>
    <div class="abs news-head" style="top:1946px">Head line Goes Here</div>
    <div class="abs news-date" style="top:1972px">My 5-2013 , Sunday 9:11 pm</div>
    <div class="abs news-text" style="top:1990px">"But I must explain to you how all this mistaken idea of denouncing pleasure and praising pain was born and I will give you a complete account of the system, and expound the actual teachings of the g</div>
    <div class="abs more" style="top:2011px">READ MORE</div>
  </section>

  <aside>
    <div class="abs share"></div>
    <div class="abs sbtn" style="left:829px;top:1767px;background:var(--blue)"><i></i>SHARE</div>
    <div class="abs sbtn light" style="left:1007px;top:1767px"><i></i>SHARE</div>
    <div class="abs sbtn" style="left:829px;top:1820px;background:var(--red)"><i></i>SHARE</div>
    <div class="abs sbtn" style="left:1007px;top:1820px;background:var(--sky)"><i></i>SHARE</div>
    <div class="abs sbtn" style="left:829px;top:1879px;background:var(--orange)"><i></i>SHARE</div>
    <div class="abs sbtn" style="left:1007px;top:1879px;background:var(--orange)"><i></i>SHARE</div>
    <div class="abs likeus">LIKE US<i></i></div>
    <div class="abs follow">Follow us<br>on Chirpline</div>
  </aside>

  <div class="abs bar" style="left:30px;top:2125px;width:743px"></div>
  <div class="abs bar" style="left:808px;top:2125px;width:359px"></div>

  <section>
    <div class="abs section-title" style="left:30px;top:2175px">POST &nbsp;YOUR COMMENT</div>
    <div class="abs field" style="top:2224px">Name</div>
    <div class="abs field" style="top:2268px">Email address</div>
    <div class="abs field" style="top:2308px">Subject</div>
    <div class="abs area">Your Comment ...</div>
    <div class="abs post">POST NOW</div>
  </section>

  <section>
    <div class="abs section-title" style="left:30px;top:2488px">LATEST VIDEO</div>
    <div class="abs video" style="left:30px;top:2547px;width:206px;height:122px"><span class="play"></span></div>
    <div class="abs video" style="left:297px;top:2547px;width:206px;height:122px"><span class="play"></span></div>
    <div class="abs video" style="left:557px;top:2547px;width:206px;height:122px"><span class="play"></span></div>
    <div class="abs vcap" style="left:30px;top:2677px">Video Heading<em>View : 700 Users</em></div>
    <div class="abs vcap" style="left:297px;top:2677px">Video Heading<em>View : 700 Users</em></div>
    <div class="abs vcap" style="left:557px;top:2677px">Video Heading<em>View : 700 Users</em></div>
  </section>

  <aside>
    <div class="abs section-title" style="left:808px;top:2175px">WHAT PEOPLE SAY ABOUT US</div>

    <div class="photo t-thumb" style="top:2224px;background:linear-gradient(135deg,#d6b08e,#8a5a3e)" role="img" aria-label="Client portrait"></div>
    <div class="abs t-name" style="top:2222px">Client Name</div>
    <div class="abs t-date" style="top:2240px">My 5-2013 , Sunday 9:11 pm</div>
    <div class="abs t-text" style="top:2256px">"But I must explain to you how all this mistaken idea of denouncing pleasure and praising pain was born and I will give you</div>
    <div class="abs t-like" style="top:2315px">Like<i></i></div>
    <div class="abs t-com" style="top:2314px">Comment</div>

    <div class="photo t-thumb" style="top:2346px;background:linear-gradient(135deg,#d6b08e,#8a5a3e)" role="img" aria-label="Client portrait"></div>
    <div class="abs t-name" style="top:2344px">Client Name</div>
    <div class="abs t-date" style="top:2362px">My 5-2013 , Sunday 9:11 pm</div>
    <div class="abs t-text" style="top:2378px">"But I must explain to you how all this mistaken idea of denouncing pleasure and praising pain was born and I will give you</div>
    <div class="abs t-like" style="top:2437px">Like<i></i></div>
    <div class="abs t-com" style="top:2436px">Comment</div>

    <div class="photo t-thumb" style="top:2468px;background:linear-gradient(135deg,#d6b08e,#8a5a3e)" role="img" aria-label="Client portrait"></div>
    <div class="abs t-name" style="top:2466px">Client Name</div>
    <div class="abs t-date" style="top:2484px">My 5-2013 , Sunday 9:11 pm</div>
    <div class="abs t-text" style="top:2500px">"But I must explain to you how all this mistaken idea of denouncing pleasure and praising pain was born and I will give you</div>
    <div class="abs t-like" style="top:2559px">Like<i></i></div>
    <div class="abs t-com" style="top:2558px">Comment</div>

    <div class="photo t-thumb" style="top:2590px;background:linear-gradient(135deg,#d6b08e,#8a5a3e)" role="img" aria-label="Client portrait"></div>
    <div class="abs t-name" style="top:2588px">Client Name</div>
    <div class="abs t-date" style="top:2606px">My 5-2013 , Sunday 9:11 pm</div>
    <div class="abs t-text" style="top:2622px">"But I must explain to you how all this mistaken idea of denouncing pleasure and praising pain was born and I will give you</div>
    <div class="abs t-like" style="top:2681px">Like<i></i></div>
    <div class="abs t-com" style="top:2680px">Comment</div>
  </aside>
</main>

<footer>
  <div class="abs footer"></div>
  <div class="abs flinks"><span>HOME</span><span>ABOUT US</span><span>SERVICES</span><span>WOMEN HEATH</span><span>PET CARE</span><span>CONTACT US</span></div>
  <div class="abs copy">All copyright are reserved by company name</div>
</footer>

</body>
</html>
```